Brevin K - Premium Business Cards

Background of Brevin K
Brevin Kaltwell is a cigar mobile lounge where guests become family. A place of luxury, relaxation, and ambiance is the global popularity demand. Brevin Kaltwell strives to provide first-class service of quality and products. Our goal is to ensure that every guest is treated and serviced as a VIP.

Brevin Kaltwell was founded by Dennis Marlow Jr in January 2020. After 15 years of cigar reviews and research Dennis decided it was time to launch his own cigar brand and boutique cigar company. With a wealth of knowledge and years of experience Brevin Kaltwell was born. With opulence for all cultures, Brevin Kaltwell offers hand rolled cigars with premium blend tobacco from sweet to bold imported from Costa Rica, Dominican Republic, and Nicaragua. Thank you for your business!

Objective:
Create a business card template to be used for all employees. Design should communicate premium and classy. And should use earth tone colors.

Design should include:
1. Client wants to incorporate the cigar leaf
2. Logo
3. Tagline: Savor Every Draw
3. Content info:
Calvin Rusholm
Owner
614-587-3906
crusholm@brevinleafco.com
brevinkaltwell.com

```html
<!DOCTYPE html>
<html lang="en">
<head>
<meta charset="utf-8">
<title>Brevin K – Business Card</title>
<link rel="stylesheet" href="https://fonts.googleapis.com/css2?family=Roboto:wght@400;500;700&family=Oswald:wght@500&display=swap">
<style>
  :root {
    --page-bg: #e6e2de;
    --card-bg: #231f20;
    --card-text: #ffffff;
    --ink: #231f20;
    --foil-light: #f4f2f2;
    --foil-mid: #d9d4d4;
    --foil-dark: #b9b2b3;
  }
  * { margin: 0; padding: 0; box-sizing: border-box; }
  html, body {
    width: 1200px;
    height: 900px;
    overflow: hidden;
    background: var(--page-bg);
  }
  .business-card {
    position: absolute;
    left: 100px;
    top: 141px;
    width: 1000px;
    height: 618px;
    background: var(--card-bg);
    color: var(--card-text);
    font-family: "Roboto", Arial, sans-serif;
    box-shadow: 0 18px 40px rgba(0,0,0,0.25);
  }
  .holder {
    position: absolute;
    left: 58px;
    top: 82px;
  }
  .holder-name {
    font-size: 36px;
    font-weight: 700;
    letter-spacing: 0.2px;
    line-height: 1.05;
    text-transform: uppercase;
  }
  .holder-role {
    font-size: 26px;
    font-weight: 400;
    line-height: 1.3;
  }
  .contact-list {
    position: absolute;
    left: 58px;
    top: 440px;
    list-style: none;
  }
  .contact-item {
    display: flex;
    align-items: center;
    gap: 9px;
    font-size: 29px;
    line-height: 37px;
    font-weight: 400;
  }
  .contact-icon {
    width: 26px;
    height: 26px;
    flex: none;
  }
  .brand-seal {
    position: absolute;
    left: 469px;
    top: 65px;
    width: 489px;
    height: 489px;
    border-radius: 50%;
    background: radial-gradient(circle at 40% 35%, var(--foil-light) 0%, var(--foil-mid) 55%, var(--foil-dark) 100%);
    color: var(--ink);
    text-align: center;
  }
  .brand-name {
    position: absolute;
    left: 0;
    right: 0;
    top: 198px;
    font-family: "Roboto", Arial, sans-serif;
    font-size: 50px;
    font-weight: 700;
    line-height: 1;
    color: var(--ink);
  }
  .brand-tagline {
    position: absolute;
    left: 0;
    right: 0;
    top: 354px;
    font-family: "Oswald", "Arial Narrow", sans-serif;
    font-weight: 500;
    font-size: 32px;
    line-height: 1.2;
    letter-spacing: 3px;
    text-transform: uppercase;
  }
</style>
</head>
<body>
  <main class="business-card">
    <div class="holder">
      <p class="holder-name">Calvin Rusholm</p>
      <p class="holder-role">Owner</p>
    </div>

    <ul class="contact-list">
      <li class="contact-item">
        <svg class="contact-icon" viewBox="0 0 24 24" aria-hidden="true">
          <path fill="#fff" d="M6.6 10.8a15.2 15.2 0 0 0 6.6 6.6l2.2-2.2c.3-.3.7-.4 1-.2 1.1.4 2.3.6 3.6.6.6 0 1 .4 1 1V20c0 .6-.4 1-1 1C10.6 21 3 13.4 3 4c0-.6.4-1 1-1h3.5c.6 0 1 .4 1 1 0 1.3.2 2.5.6 3.6.1.3 0 .7-.2 1z"/>
          <path fill="none" stroke="#fff" stroke-width="1.6" d="M14 3.5a6.5 6.5 0 0 1 6.5 6.5M14 7a3 3 0 0 1 3 3"/>
        </svg>
        <span>614-587-3906</span>
      </li>
      <li class="contact-item">
        <svg class="contact-icon" viewBox="0 0 24 24" aria-hidden="true">
          <rect x="2" y="5" width="20" height="14" fill="#fff"/>
          <path fill="none" stroke="#231f20" stroke-width="1.6" d="M2.5 5.5 12 13l9.5-7.5M2.5 18.5l7-6.5M21.5 18.5l-7-6.5"/>
        </svg>
        <span>crusholm@brevinleafco.com</span>
      </li>
      <li class="contact-item">
        <svg class="contact-icon" viewBox="0 0 24 24" aria-hidden="true">
          <g fill="none" stroke="#fff" stroke-width="1.6">
            <circle cx="12" cy="12" r="9.5"/>
            <ellipse cx="12" cy="12" rx="4" ry="9.5"/>
            <path d="M2.5 12h19M4 7h16M4 17h16"/>
          </g>
        </svg>
        <span>brevinkaltwell.com</span>
      </li>
    </ul>

    <div class="brand-seal">
      <p class="brand-name">Brevin Kaltwell</p>
      <p class="brand-tagline">Savor Every Draw</p>
    </div>
  </main>
</body>
</html>
```